Boutique Sparkling Blanc de Blancs Wine label

We are looking for a label and neck label for our new Sparkling Chardonnay.
Images uploaded include, bubbles and glitter maybe as a faded background for whole label?
We like Refined, elegant yet simple designs.
Have included our current table chardonnay label as example.

Industry/Entity Type

Boutique

Font styles to use
Decorative
Script

Requirements
Must have
• Name - "Every Moonlit Hour"
• Methode Traditionelle
• Blanc de Blancs
• 2015
• Beyond the Orchards (Brand)
• Adelaide Hills
Nice to have
• Neutral tones
• Sparkles, Glitter, Bubbles
• Traditional, cursive or vine like fonts
• Have attached fonts we used for previous wine label - might be nice to carry through same/similar fonts to continue our brand?
Should not have
• a lot of colour

```html
<!DOCTYPE html>
<html lang="en">
<head>
<meta charset="utf-8">
<title>Every Moonlit Hour – Blanc de Blancs Label</title>
<link rel="stylesheet" href="https://fonts.googleapis.com/css2?family=Great+Vibes&family=Cinzel:wght@400;600&display=swap">
<style>
  :root {
    --backdrop-top: #f4f4f4;
    --backdrop-bottom: #dcdcdc;
    --label-edge: #ffffff;
    --label-cream-light: #fdf8dc;
    --label-cream: #f5e9ae;
    --label-gold: #7a5a16;
    --vintage-gold: #c9a43a;
    --ink-brown: #5c4210;
    --neck-foil: #1d1d1b;
  }
  * { margin: 0; padding: 0; box-sizing: border-box; }
  html, body {
    width: 801px;
    height: 1200px;
    overflow: hidden;
  }
  body {
    background: linear-gradient(180deg, var(--backdrop-top) 0%, var(--backdrop-bottom) 100%);
    position: relative;
  }
  .front-label {
    position: absolute;
    left: 50px;
    top: 150px;
    width: 700px;
    height: 660px;
  }
  .front-label__shape {
    position: absolute;
    inset: 0;
    filter: drop-shadow(0 3px 6px rgba(0,0,0,0.12));
  }
  .ornament {
    position: absolute;
    left: 50%;
    transform: translateX(-50%);
    border-radius: 40px;
  }
  .ornament--crest {
    top: 38px;
    width: 130px;
    height: 30px;
    background: linear-gradient(180deg, rgba(122,90,22,0.15), rgba(122,90,22,0.45));
  }
  .ornament--vine {
    width: 580px;
    height: 56px;
    background: linear-gradient(90deg, rgba(122,90,22,0.08) 0%, rgba(122,90,22,0.5) 25%, rgba(122,90,22,0.6) 50%, rgba(122,90,22,0.5) 75%, rgba(122,90,22,0.08) 100%);
  }
  .ornament--vine-upper { top: 272px; }
  .ornament--vine-lower { top: 474px; }
  .wine-name {
    position: absolute;
    top: 78px;
    left: 0;
    width: 100%;
    text-align: center;
    font-family: "Great Vibes", cursive;
    font-size: 58px;
    line-height: 56px;
    color: var(--ink-brown);
  }
  .wine-details {
    position: absolute;
    top: 350px;
    left: 0;
    width: 100%;
    list-style: none;
    text-align: center;
    font-family: "Cinzel", serif;
    font-size: 24px;
    letter-spacing: 2px;
    line-height: 38px;
    color: var(--ink-brown);
  }
  .vintage {
    position: absolute;
    top: 558px;
    left: 0;
    width: 100%;
    text-align: center;
    font-family: "Cinzel", serif;
    font-weight: 600;
    font-size: 24px;
    letter-spacing: 3px;
    color: var(--vintage-gold);
  }
  .neck-label {
    position: absolute;
    left: 150px;
    top: 900px;
    width: 500px;
    height: 56px;
    background: var(--neck-foil);
    border-bottom: 4px solid var(--vintage-gold);
    display: flex;
    align-items: center;
    justify-content: center;
    font-family: "Cinzel", serif;
    font-size: 20px;
    letter-spacing: 4px;
    color: var(--vintage-gold);
  }
</style>
</head>
<body>
  <section class="front-label">
    <svg class="front-label__shape" viewBox="0 0 700 660" width="700" height="660" aria-hidden="true">
      <defs>
        <radialGradient id="cream-fill" cx="50%" cy="45%" r="65%">
          <stop offset="0%" stop-color="var(--label-cream-light)"/>
          <stop offset="100%" stop-color="var(--label-cream)"/>
        </radialGradient>
      </defs>
      <path fill="var(--label-edge)" d="M180,250 L180,190 A170,170 0 0 1 520,190 L520,250 L600,250 L700,320 L700,540 L350,640 L0,540 L0,320 L100,250 Z"/>
      <path fill="url(#cream-fill)" stroke="var(--label-gold)" stroke-width="3" d="M192,262 L192,190 A158,158 0 0 1 508,190 L508,262 L596,262 L688,326 L688,532 L350,627 L12,532 L12,326 L104,262 Z"/>
    </svg>

    <div class="ornament ornament--crest" role="img" aria-label="Small scrolled crest ornament"></div>
    <h1 class="wine-name">Every Moonlit<br>Hour</h1>
    <div class="ornament ornament--vine ornament--vine-upper" role="img" aria-label="Grapevine border with grape clusters and leaves"></div>
    <ul class="wine-details">
      <li>Methode Traditionelle</li>
      <li>Blanc de Blancs</li>
      <li>Adelaide Hills</li>
    </ul>
    <div class="ornament ornament--vine ornament--vine-lower" role="img" aria-label="Grapevine border with grape clusters and leaves"></div>
    <p class="vintage">2015</p>
  </section>

  <aside class="neck-label">BEYOND THE ORCHARDS</aside>
</body>
</html>
```